Construction Company informative web page

Lorvane Builders is a new company that combine Project Manager and kitchen & bath design with Interior remodeling for houses or business (commercial and residential construction)
We want to show our reviews, portafolio and background experience
Updates

Reason: I would like to have the time to interact with the favorite designers to fine tune the website also I'd like to see more designs

Hello Everybody,

Thank you for your time, please make the corrections shown below:

Pages:

1. Home:

1.  Includes a welcome and a briefly background:

2. Right side vertically show a few reviews with the option read more to open it, just the Name and last name, city and review (no start ratings)

3. Facebook and youtube link

4. Left side below shows 4 slides show with pictures and titles:

1. Kitchen Design

2. Bath Design

3. General Remodeling

4. Commercial Projects

2. About Us:

Our Professionals:

Lorvane Builders Project Manager  is responsible to set the project schedule, request materials  and coordinate the delivery on time.  The Project Manager focus is ensuring  the best customer satisfaction in every step of the project until the final product is completed.

The Designer gives you the best ideas in 3D format,   getting the best lay out possible.  understanding your needs, defining your unique style putting together all your requirements and ideas to make the best match for you, making sure you get the best products within your budget

Lorvane Builders have a high quality group of trade specialist; plumbers, electricians and installers. Our crew is pleasant to work with,  safety and cleaning values  and very detailed oriented

Our Core Values

As our slogan your project is our business, well we really mean it our job is not just to do the job is to guaranteed a pleasant experience with great costumer service, communication, quality, in time and within your budget

 

1. Services:

1. Commercial

2. Residential

2. Portafolio:  Separated pictures in each project, I want to have a brief description in each picture

1. Kitchen Design

2. Bath Design

3. General Remodeling

4. Commercial Projects

 

1. Contact Us:  

1. Project Management Department:

Contact Person: Tessa Kobrin

Email: tessa@lorvanebuilders.com

2. Office Management Department:

Contact Person: Rue Fendwick

Email: info@lorvanebuilders.com

 

Please try to pick design style shown in business card to match a little bit. Keep the color tones

I want the logo in the upper left corner and a very nice picture with a kitchen (warm colors)mostly American northeast style like the main pic of the web.

I want the web page is able to be fully open in computers, tablets and cellphones

Please send me an email to lorvanebuild7@mailbrook.net so I can send you my logo and any other information to be incorporated

Thank you

Hello Everybody,

Thank you for your time, please make the corrections accordingly:

Pages:

1. Home: Includes a welcome and a briefly say something about our background 

Hello, I just upload my logo and my business card so you can adjust your designs

Please presented responsive format

I want coding the webpage too

Please read carefully my last update

Thank you so much!                                   

Industry/Entity Type

Residential

Requirements
Nice to have
• Should it has a Newsletter subscription with the email at the bottom of the home page
In contact page: A box "Contact us for a free estimate"

```html
<!DOCTYPE html>
<html lang="en">
<head>
<meta charset="utf-8">
<title>Lorvane Builders</title>
<link rel="stylesheet" href="https://fonts.googleapis.com/css2?family=Oswald:wght@300;400;500&family=Open+Sans:wght@400;600&display=swap">
<style>
:root{
  --maroon:#7a2320;
  --maroon-dark:#5e1a18;
  --tan:#e4c48b;
  --tan-light:#efd9a8;
  --cream:#f4eedd;
  --paper:#f8f7f5;
  --rose:#b25f5c;
  --brown:#8c5b44;
  --ink:#333;
  --body:#555;
  --white:#fff;
}
*{box-sizing:border-box;margin:0;padding:0}
html,body{width:900px;height:1200px;overflow:hidden}
body{position:relative;background:var(--cream);font-family:"Open Sans",Arial,sans-serif;color:var(--body)}
.top-band{position:absolute;left:0;top:0;width:900px;height:72px;background:var(--tan)}
.header{position:absolute;left:15px;top:14px;width:870px;height:83px;background:var(--maroon);border-radius:4px;box-shadow:0 4px 6px rgba(0,0,0,.15)}
.brand{position:absolute;left:16px;top:12px;display:flex;align-items:center;gap:8px}
.brand-mark{width:22px;height:22px;background:var(--tan)}
.brand-name{font-family:"Oswald",sans-serif;font-weight:400;font-size:17px;color:var(--white);line-height:1.1;width:70px}
.divider{position:absolute;left:112px;top:12px;width:1px;height:58px;background:rgba(255,255,255,.25)}
.call{position:absolute;left:143px;top:26px;display:flex;align-items:center;gap:10px;color:var(--white);font-family:"Oswald",sans-serif;font-size:22px}
.call .num{font-weight:300;font-size:21px;margin-left:4px}
.social{position:absolute;right:16px;top:21px;display:flex;gap:11px}
.social span{width:41px;height:41px;border-radius:50%;background:var(--cream)}
.nav{position:absolute;left:15px;top:122px;width:870px;height:46px;background:linear-gradient(#f0d9a9,#e1c088);border:1px solid #d8b77c;border-radius:4px 4px 0 0;display:flex}
.nav a{font-family:"Oswald",sans-serif;font-size:18px;color:#6b4030;text-decoration:none;display:flex;align-items:center;padding:0 27px;border-right:1px solid #c9a46b;height:100%}
.nav a.active{color:var(--maroon)}
.hero{position:absolute;left:15px;top:167px;width:870px;height:347px;background:linear-gradient(100deg,#6a3a22 0%,#a8683c 30%,#d8a770 48%,#8e4b2e 65%,#b06a4a 85%,#7d3a28 100%)}
.hero-title{position:absolute;left:15px;top:398px;width:353px;height:50px;background:rgba(228,196,139,.85);font-family:"Oswald",sans-serif;font-size:27px;color:var(--maroon);display:flex;align-items:center;padding-left:26px}
.contact{position:absolute;left:645px;top:195px;width:230px;height:255px;background:rgba(228,196,139,.78);border-top:10px solid var(--maroon)}
.contact h2{font-family:"Oswald",sans-serif;font-weight:400;font-size:25px;color:#2a1a14;text-align:center;margin-top:12px}
.field{position:absolute;left:13px;width:204px;background:var(--maroon);color:#f4e3d0;font-size:14px;padding:6px 13px}
.btn{position:absolute;left:68px;top:205px;width:95px;height:30px;background:#2b2b2b;color:var(--white);font-size:16px;display:flex;align-items:center;justify-content:center}
.arrow{position:absolute;top:463px;width:34px;height:34px;background:var(--maroon);display:flex;align-items:center;justify-content:center}
.welcome{position:absolute;left:15px;top:514px;width:870px;height:231px;background:var(--paper);text-align:center}
.welcome h1{font-family:"Oswald",sans-serif;font-weight:400;font-size:30px;color:var(--ink);margin-top:19px}
.welcome h1 em{font-style:normal;color:var(--maroon)}
.welcome .tag{font-family:"Open Sans",sans-serif;font-size:21px;color:#555;margin-top:6px;letter-spacing:.3px}
.rule{width:780px;height:2px;margin:14px auto 0;background:linear-gradient(90deg,transparent,#ccc,transparent)}
.welcome p{font-size:13px;line-height:21px;color:#555;width:840px;margin:13px auto 0}
.welcome p b{font-weight:400;color:var(--maroon)}
.more{display:inline-flex;align-items:center;gap:7px;font-family:"Oswald",sans-serif;font-weight:300;font-size:20px;color:#6b3a2c;margin-top:8px}
.card{position:absolute;top:774px;width:272px;height:363px;background:var(--paper)}
.card h3{font-family:"Oswald",sans-serif;font-weight:300;font-size:21px;color:var(--ink);padding:12px 15px 0;height:48px}
.tile{position:absolute;left:0;width:272px;height:138px}
.tile .cap{position:absolute;left:0;bottom:0;width:100%;height:32px;background:rgba(30,30,30,.7);color:var(--white);font-size:16px;text-align:center;line-height:32px}
.see{position:absolute;left:0;top:327px;width:272px;height:36px;background:var(--brown);color:var(--white);font-size:18px;padding:0 13px;display:flex;align-items:center;justify-content:space-between}
.reviews{position:absolute;left:613px;top:774px;width:272px;height:363px;background:var(--rose)}
.reviews h3{font-family:"Oswald",sans-serif;font-weight:300;font-size:21px;color:var(--white);padding:12px 18px 0;height:47px;border-bottom:1px solid rgba(255,255,255,.6)}
.review{display:flex;justify-content:space-between;align-items:center;padding:0 11px 0 19px;height:44px;border-bottom:1px solid rgba(255,255,255,.6);color:var(--white);font-size:15px}
.review.open{background:var(--tan);height:89px;align-items:flex-start;padding-top:12px;color:var(--maroon);display:block;position:relative}
.review.open p{color:#333;font-size:13px;line-height:20px;margin-top:4px}
.review.open svg{position:absolute;right:11px;top:12px}
.footer{position:absolute;left:0;top:1165px;width:900px;height:35px;background:var(--maroon);color:var(--white);font-size:13px;padding:0 15px;display:flex;align-items:center}
</style>
</head>
<body>
<div class="top-band"></div>

<header class="header">
  <div class="brand"><span class="brand-mark"></span><span class="brand-name">Lorvane Builders</span></div>
  <div class="divider"></div>
  <div class="call">
    <svg width="17" height="17" viewBox="0 0 24 24"><path fill="#fff" d="M6.6 10.8c1.4 2.8 3.8 5.1 6.6 6.6l2.2-2.2c.3-.3.7-.4 1-.2 1.1.4 2.3.6 3.6.6.6 0 1 .4 1 1V20c0 .6-.4 1-1 1C10.6 21 3 13.4 3 4c0-.6.4-1 1-1h3.5c.6 0 1 .4 1 1 0 1.3.2 2.5.6 3.6.1.3 0 .7-.2 1z"/></svg>
    <span>FEEL FREE TO CALL US!</span><span class="num">+215-555-0147</span>
  </div>
  <div class="social"><span aria-label="Social link"></span><span aria-label="Social link"></span><span aria-label="Social link"></span></div>
</header>

<nav class="nav">
  <a class="active">HOME</a><a>ABOUT</a><a>FEATURES</a><a>PROTFOLIO</a><a>BLOG</a><a>CONTACT</a>
</nav>

<div class="hero" role="img" aria-label="Warm wood kitchen with stone island and pendant lights"></div>
<div class="hero-title">LOREM IPSUM &amp; DOLOR AMET!</div>

<form class="contact">
  <h2>CONTACT US</h2>
  <div class="field" style="top:50px;height:31px">Name</div>
  <div class="field" style="top:91px;height:31px">Email</div>
  <div class="field" style="top:131px;height:64px">Description</div>
  <div class="btn">Submit</div>
</form>
<div class="arrow" style="left:797px"><svg width="12" height="16" viewBox="0 0 12 16"><path d="M9 2 3 8l6 6" stroke="#fff" stroke-width="3" fill="none"/></svg></div>
<div class="arrow" style="left:837px"><svg width="12" height="16" viewBox="0 0 12 16"><path d="m3 2 6 6-6 6" stroke="#fff" stroke-width="3" fill="none"/></svg></div>

<section class="welcome">
  <h1>Welcome to <em>Lorvane Builders</em> Website</h1>
  <div class="tag">simply dummy text of the printing and typesetting industry.</div>
  <div class="rule"></div>
  <p>It is a long established fact that a reader will be <b>distracted</b> by the readable content of a page when looking at its layout. The point of using Lorem Ipsum is that it has a more-or-less normal distribution of letters, as opposed to using <b>'Content here, content here'</b>, making it look like readable English. Many desktop publishing packages and web page editors now use</p>
  <span class="more">learn more <svg width="19" height="19" viewBox="0 0 20 20"><circle cx="10" cy="10" r="10" fill="#8c4a3c"/><path d="M5 10h9M10 6l4 4-4 4" stroke="#fff" stroke-width="2.4" fill="none"/></svg></span>
</section>

<section class="card" style="left:15px">
  <h3>PORTAFOLIO</h3>
  <div class="tile" style="top:48px;background:linear-gradient(#e6e2dc,#b7b2ab)" role="img" aria-label="White bathroom with tub and basin"><div class="cap">Variations of Passages</div></div>
  <div class="tile" style="top:188px;background:linear-gradient(#d9d6d0,#6d6a66)" role="img" aria-label="Kitchen with white cabinets and dark counter"><div class="cap">Established Fact</div></div>
  <div class="see">See All <svg width="22" height="22" viewBox="0 0 22 22"><circle cx="11" cy="11" r="11" fill="#fff"/><path d="m9 6 5 5-5 5" stroke="#8c5b44" stroke-width="2.6" fill="none"/></svg></div>
</section>

<section class="card" style="left:315px">
  <h3>BACKGROUND EXPERIENCE</h3>
  <div class="tile" style="top:48px;background:linear-gradient(#3b2a20,#8a4b2d 60%,#4a3328)" role="img" aria-label="Dark wood kitchen with red tiled wall"><div class="cap">Specimen Book</div></div>
  <div class="tile" style="top:188px;background:linear-gradient(#e8e6ea,#6e5d88)" role="img" aria-label="Bathroom with purple wall and white tub"><div class="cap">Lorem Ipsum Available</div></div>
  <div class="see">See All <svg width="22" height="22" viewBox="0 0 22 22"><circle cx="11" cy="11" r="11" fill="#fff"/><path d="m9 6 5 5-5 5" stroke="#8c5b44" stroke-width="2.6" fill="none"/></svg></div>
</section>

<section class="reviews">
  <h3>REVIEWS</h3>
  <div class="review">Lorem Ipsum used since <svg width="20" height="20" viewBox="0 0 20 20"><circle cx="10" cy="10" r="10" fill="#fff"/><path d="M10 5v10M5 10h10" stroke="#b25f5c" stroke-width="2.4"/></svg></div>
  <div class="review open">Lorem Ipsum used since <svg width="20" height="20" viewBox="0 0 20 20"><circle cx="10" cy="10" r="10" fill="#fff"/><path d="M5 10h10" stroke="#b25f5c" stroke-width="2.4"/></svg><p>Lorem ipsum dolor sit amet conse ctetur adipisicing elit,</p></div>
  <div class="review">Lorem Ipsum used since <svg width="20" height="20" viewBox="0 0 20 20"><circle cx="10" cy="10" r="10" fill="#fff"/><path d="M10 5v10M5 10h10" stroke="#b25f5c" stroke-width="2.4"/></svg></div>
  <div class="review">Lorem Ipsum used since <svg width="20" height="20" viewBox="0 0 20 20"><circle cx="10" cy="10" r="10" fill="#fff"/><path d="M10 5v10M5 10h10" stroke="#b25f5c" stroke-width="2.4"/></svg></div>
  <div class="review">Lorem Ipsum used since <svg width="20" height="20" viewBox="0 0 20 20"><circle cx="10" cy="10" r="10" fill="#fff"/><path d="M10 5v10M5 10h10" stroke="#b25f5c" stroke-width="2.4"/></svg></div>
  <div class="review" style="border-bottom:0">Lorem Ipsum used since <svg width="20" height="20" viewBox="0 0 20 20"><circle cx="10" cy="10" r="10" fill="#fff"/><path d="M10 5v10M5 10h10" stroke="#b25f5c" stroke-width="2.4"/></svg></div>
</section>

<footer class="footer">Lorvane Builders © 2014. Privacy Policy</footer>
</body>
</html>
```